Tobrin Pelmo Broth is looking for a DL Flyer for their unique food the #velmorabroth

We're looking for a punchy flyer which depicts our food dish and includes a small blurb on the front & back. Flyer size is portrait style DL (210 x 99mm) & must be 'Press Ready Files'.
Brief: Flyer background is light wooden chopping board with vertical strips.

(Text: Calibri Body or similar text, must be easy to read! Minimum 50% width)
TvR proudly present..
(Text: Calibri Body Header or similar text, must be easy to read! Min. 75% width) PELMO BROTH

Below the text PELMO BROTH insert an image (size is approx 25% of Flyer) of Borneo with a reference to Kuching. Map of Borneo can be an outline or similar but not too prominent.
Overlay the top of the map with the following text in Monotype Corsivab or similar! but must be easy to read.
Text: Kuching (2 sizes larger) Capital City of Sarawak on the Island of Borneo is home to some of the world’s greatest and unique dishes.
(new line) TvR will take you on a culinary journey to Kuching with a favourite local dish the
(new line) #VelmoraBroth (double space) so sit back, relax & enjoy!

Insert and centre the attached image DSC_0927.JPG
Remove the spoon and make the image more vibrant, do not change the colour of the soup.
Refer to attached file Flyer.jpg for images of chopsticks, a boiled egg and ingredients at the bottom. We like the lines to point to key ingredients e.g. to the egg, prawns etc. current design the font is difficult to read.

List contact details toward the bottom.
e: TvR.PelmoBroth@quillmail.example
m: +61 437152096
f : Tobrin Pelmo Broth

on the reverse of the Flyer:
Background is light wooden chopping board with vertical strips, same as front.

Refer to below link for text & Nutritional Values table.
The text for the main four paragraphs should be the key note and majority.
Note the Ingredients and the Nutritional Values table size is max 12.5% of the total Flyer size.

https://files.dorvanshare.example/doc/7QmTx83LwPzR2nVb5KcYe0HsJd4UfAi6Go1tNr9/edit

Target Market(s)

An international foody with a sense of adventure. The dish is nutritional, Gluten Free and a healthy meal. It will be sold at food markets, to office workers for lunch and for a lighter evening meal.

Industry/Entity Type

Food Production

Colors

Designer to choose colors to be used in the design.

Requirements
Must have
• 'TvR proudly present..' must be a statement along with the product 'PELMO BROTH'
• The map of Borneo with reference to Kuching, the home of the product.
• A picture of the dish itself.

```html
<!DOCTYPE html>
<html lang="en">
<head>
<meta charset="utf-8">
<title>Pelmo Broth DL Flyer</title>
<link rel="stylesheet" href="https://fonts.googleapis.com/css2?family=Open+Sans:ital,wght@0,400;0,600;0,700;1,400&family=Cormorant+Garamond:ital,wght@1,500;1,700&display=swap">
<style>
  :root {
    --stage: #d9a514;
    --board-light: #f1f1ef;
    --board-mid: #dcdcda;
    --seam: rgba(120,120,120,0.18);
    --accent: #e2572a;
    --ink: #1d1d1d;
    --ink-soft: #333;
    --rule: #444;
  }
  * { box-sizing: border-box; margin: 0; padding: 0; }
  html, body { width: 1200px; height: 1200px; overflow: hidden; }
  body {
    background: var(--stage);
    font-family: "Open Sans", Arial, sans-serif;
    color: var(--ink);
    position: relative;
  }
  .flyer {
    position: absolute;
    top: 70px;
    width: 500px;
    height: 1060px;
    overflow: hidden;
    background:
      repeating-linear-gradient(90deg, transparent 0 61px, var(--seam) 61px 63px, transparent 63px 125px),
      linear-gradient(90deg, var(--board-light), var(--board-mid) 30%, var(--board-light) 55%, var(--board-mid) 80%, var(--board-light));
    box-shadow: 0 6px 18px rgba(0,0,0,0.25);
  }
  .flyer--front { left: 70px; }
  .flyer--back { left: 630px; }

  .placeholder { position: absolute; }

  /* front */
  .front__title {
    position: absolute; top: 36px; left: 30px; right: 20px;
    font-weight: 700; font-size: 47px; letter-spacing: 0.5px;
    color: var(--accent); text-align: center;
  }
  .front__blurb {
    position: absolute; top: 118px; left: 30px; width: 430px;
    font-family: "Cormorant Garamond", Georgia, serif; font-style: italic; font-weight: 500;
    font-size: 16px; line-height: 1.2; color: var(--ink);
  }
  .front__blurb p { margin-bottom: 16px; }
  .front__blurb .place { font-family: "Open Sans", Arial, sans-serif; font-style: normal; font-weight: 700; font-size: 19px; }
  .map { left: 300px; top: 205px; width: 140px; height: 100px; border-radius: 40% 50% 45% 40%;
    background: radial-gradient(ellipse at 50% 50%, #dfe6dc, #c9d2c6); opacity: 0.9; }
  .dish { left: 15px; top: 330px; width: 400px; height: 400px; border-radius: 50%;
    background: radial-gradient(circle at 50% 48%, #b4532e 0 34%, #d08a55 45%, #f6f5f2 58%, #ecebe7 100%);
    box-shadow: 0 4px 12px rgba(0,0,0,0.15); }
  .chopsticks { left: 420px; top: 330px; width: 24px; height: 320px; transform: rotate(-14deg);
    background: linear-gradient(90deg, #d9b07a, #e8c799, #c99a5d); border-radius: 4px; }
  .herb-left { left: -10px; top: 650px; width: 80px; height: 110px; border-radius: 50%;
    background: radial-gradient(circle, #4d9a35, #2f7a23); }
  .herb-right { left: 440px; top: 735px; width: 70px; height: 70px; border-radius: 50%;
    background: radial-gradient(circle, #5aa83e, #327f25); }
  .ingredients { left: 0; right: 0; bottom: 0; height: 150px;
    background: linear-gradient(90deg, #8fb061 0%, #c9a06a 28%, #9e2f22 50%, #e9dfcf 75%, #6ea145 100%); opacity: 0.9; }
  .callout {
    position: absolute; font-family: "Cormorant Garamond", Georgia, serif; font-style: italic; font-weight: 500;
    font-size: 19px; color: var(--ink); line-height: 1;
  }
  .leaders { position: absolute; inset: 0; pointer-events: none; }
  .contact { position: absolute; top: 810px; left: 95px; font-size: 21px; color: var(--ink-soft); }
  .contact li { list-style: none; display: flex; align-items: center; gap: 8px; margin-bottom: 5px; }
  .contact svg { width: 18px; height: 18px; flex: none; }
  .contact .dot { width: 16px; height: 16px; border-radius: 50%; border: 1.5px solid var(--ink-soft); flex: none; }

  /* back */
  .back__copy { position: absolute; top: 48px; left: 42px; right: 36px; font-size: 12.6px; line-height: 1.3; color: var(--ink); }
  .back__copy p { margin-bottom: 16px; text-align: justify; }
  .back__copy .gap { margin-top: 34px; }
  .hl { color: var(--accent); font-weight: 600; }
  .back__copy .ingredients-list { font-size: 13.4px; }
  .back__copy .ingredients-list em { font-style: italic; }
  .nutrition {
    position: absolute; top: 790px; left: 55px; width: 430px;
    border-collapse: collapse; font-size: 15px;
  }
  .nutrition th { background: var(--accent); color: #fff; text-align: left; font-weight: 600; padding: 5px 12px; border: 1px solid var(--rule); vertical-align: top; line-height: 1.2; }
  .nutrition th:first-child { color: var(--ink); }
  .nutrition td { padding: 3px 14px; border-bottom: 1px solid var(--rule); font-weight: 600; }
  .nutrition td:last-child { font-weight: 400; border-left: 1px solid var(--rule); }
  .nutrition tr.sub td:first-child { padding-left: 120px; }
  .nutrition tbody { border: 1px solid var(--rule); }
  .chilli-corner { left: 0; bottom: 0; width: 80px; height: 60px; background: radial-gradient(circle at 20% 80%, #9b2a1f, transparent 70%); }
  .basil-corner { right: 0; bottom: 0; width: 110px; height: 80px; background: radial-gradient(circle at 70% 70%, #4f9c37, transparent 70%); }
</style>
</head>
<body>

<section class="flyer flyer--front">
  <h1 class="front__title">PELMO BROTH</h1>
  <div class="placeholder map" role="img" aria-label="Outline map of Borneo with a pin marking Kuching"></div>
  <div class="front__blurb">
    <p><span class="place">Kuching</span> Capital City of Sarawak on the Island of Borneo is home to some of the world’s greatest and unique dishes.</p>
    <p>TvR will take you on a culinary journey to Kuching with a favourite local dish the</p>
    <p>#VelmoraBroth&nbsp; so sit back, relax &amp; enjoy!</p>
  </div>

  <div class="placeholder chopsticks" role="img" aria-label="Pair of wooden chopsticks"></div>
  <div class="placeholder dish" role="img" aria-label="Bowl of broth with noodles, chicken, prawns, omelette strips, bean curd and a halved boiled egg"></div>
  <div class="placeholder herb-left" role="img" aria-label="Fresh basil leaves"></div>
  <div class="placeholder herb-right" role="img" aria-label="Fresh basil leaf"></div>

  <span class="callout" style="top:300px;left:28px;">Chicken breast</span>
  <span class="callout" style="top:278px;left:175px;">King Prawns</span>
  <span class="callout" style="top:695px;left:395px;text-align:center;">Fried bean<br>curd</span>
  <span class="callout" style="top:735px;left:20px;">Free Range Egg</span>

  <svg class="leaders" viewBox="0 0 500 1060">
    <g stroke="#333" stroke-width="0.8" fill="none">
      <line x1="70" y1="322" x2="110" y2="430"/>
      <line x1="215" y1="300" x2="205" y2="470"/>
      <line x1="420" y1="692" x2="335" y2="520"/>
      <line x1="85" y1="733" x2="155" y2="640"/>
      <line x1="115" y1="788" x2="435" y2="788"/>
    </g>
  </svg>

  <div class="placeholder ingredients" role="img" aria-label="Fresh ingredients: lemongrass, ginger, dried chillies, garlic and coriander"></div>

  <ul class="contact">
    <li>
      <svg viewBox="0 0 18 18"><rect x="1" y="4" width="16" height="11" fill="#333"/><path d="M1 4 L9 10 L17 4" stroke="#fff" stroke-width="1.2" fill="none"/></svg>
      TvR.PelmoBroth@quillmail.example
    </li>
    <li>
      <svg viewBox="0 0 18 18"><rect x="1" y="1" width="16" height="16" rx="3" fill="#333"/><path d="M6 4 C4 6 5 10 8 13 C10 14.5 12 15 13.5 13.5 L12 11.5 L10.5 12 C9 11 7.5 9.5 7 8 L7.6 6.5 Z" fill="#fff"/></svg>
      +61 437152096
    </li>
    <li><span class="dot"></span>Tobrin Pelmo Broth</li>
  </ul>
</section>

<section class="flyer flyer--back">
  <div class="back__copy">
    <p><span class="hl">Roaming Plates:</span> a short while ago on my travels around East Malaysia I was introduced to a place called Kuching, Capital City of Sarawak.</p>
    <p>I was overwhelmed by their number of unique dishes, from the Sea to the Borneo Jungle local sustainable ingredients are sourced to create some of Kuching’s indigenous foods.</p>
    <p>I was astonished to learn that famous Kuching dishes like Kolo Mee and the Velmora Broth are breakfast dishes and often sold out by 10am.</p>
    <p>I have chosen the <span class="hl">Velmora Broth</span> to share with You… It converts perfectly to our requirements - a healthy, <strong>Gluten-Free</strong> nourishing meal, although maybe not breakfast for everyone!</p>
    <p class="gap"><span class="hl">The Broth sambal</span> / base stock is made from ALL plant-based ingredients.</p>
    <p>We add a dash of coconut milk to bring balance to this simple yet complex dish; with it’s more subtle and fine blend of aromatic herbs and spices and a hint of sour and chilli undertones.</p>
    <p class="ingredients-list"><strong>Ingredients:</strong> <em>rice vermicelli - bihoon, omelette strips (free range eggs), sliced chicken breast, King prawns, bean-sprouts, fried bean curd and garnished with lime wedge, fresh coriander and sambal on the side.</em></p>
  </div>

  <table class="nutrition">
    <thead>
      <tr><th>NUTRITION INFORMATION:</th><th>Pelmo Broth<br>Per serve</th></tr>
    </thead>
    <tbody>
      <tr><td>ENERGY</td><td>1920 kj</td></tr>
      <tr><td>CALORIES</td><td>458</td></tr>
      <tr><td style="border-bottom:none;">PROTEIN</td><td style="border-bottom:none;">30g</td></tr>
      <tr class="sub"><td>-GLUTEN</td><td>UNDETECTED</td></tr>
      <tr><td>FAT - TOTAL</td><td>38g</td></tr>
      <tr><td>CARBOHYDRATES</td><td>52g</td></tr>
    </tbody>
  </table>

  <div class="placeholder chilli-corner" role="img" aria-label="Dried red chillies"></div>
  <div class="placeholder basil-corner" role="img" aria-label="Fresh basil leaves"></div>
</section>

</body>
</html>
```